Commercial Piping Company Needs A Modern Business Card

We need a clean business card for our commercial pipe lining company. We would like to see a mock up in two color schemes: Black, Grey and Blue and Black, Grey and Orange. We are in the piping industry, but want a professional, clean and modern look to the card.

Industry/Entity Type

Plumbing

Contact Information for Business Card

Name: Mark Tollen
Title: Managing Partner
Phone: 382.615.9073
Email: Mark@VantoPipe.Net

Requirements
Must have
• Back Side Should Have a White Back Ground with Full Logo. Front I would like to see a couple lay outs for contact info. Also the final card will have rounded edges, so please take that into account for printing.
Nice to have
• Two Color Palette Examples
Should not have
• No need for an address line

```html
<!DOCTYPE html>
<html lang="en">
<head>
<meta charset="utf-8">
<title>VantoPipe Business Card</title>
<link href="https://fonts.googleapis.com/css2?family=Montserrat:wght@400;500;600&display=swap" rel="stylesheet">
<style>
  :root {
    --backdrop: #1d1d1d;
    --card: #ffffff;
    --ink: #111111;
    --brand-blue: #0067a3;
    --rule: #9ec8e4;
  }
  * { margin: 0; padding: 0; box-sizing: border-box; }
  html, body { width: 1200px; height: 1200px; overflow: hidden; }
  body { background: var(--backdrop); font-family: "Montserrat", sans-serif; position: relative; }
  .card {
    position: absolute; top: 240px; width: 411px; height: 720px;
    border-radius: 42px; background: var(--card); overflow: hidden;
  }
  .card--back { left: 123px; }
  .card--front { left: 652px; }

  .mark-dot { position: absolute; border-radius: 50%; background: var(--ink); }
  .card--back .mark-dot { left: 125px; top: 230px; width: 160px; height: 160px; }

  .wordmark { position: absolute; left: 0; right: 0; text-align: center; color: var(--ink); font-weight: 500; line-height: 1; white-space: nowrap; }
  .card--back .wordmark { top: 401px; font-size: 56px; letter-spacing: 1px; }
  .card--front .wordmark { top: 52px; font-size: 42px; letter-spacing: 1px; }

  .tagline { position: absolute; left: 0; right: 0; text-align: center; color: var(--ink); font-weight: 400; line-height: 1; white-space: nowrap; }
  .card--back .tagline--primary { top: 456px; font-size: 17.5px; letter-spacing: 2.6px; }
  .card--back .tagline--secondary { top: 477px; font-size: 16px; letter-spacing: 4.4px; }
  .card--front .tagline--primary { top: 99px; font-size: 13.5px; letter-spacing: 1.9px; }
  .card--front .tagline--secondary { top: 115px; font-size: 12.5px; letter-spacing: 3.2px; }

  .contact-panel { position: absolute; left: 0; right: 0; top: 360px; bottom: 0; background: var(--brand-blue); }
  .front-ring { position: absolute; left: 111px; top: 248px; width: 188px; height: 188px; border-radius: 50%; background: var(--card); }
  .card--front .mark-dot { left: 129px; top: 266px; width: 152px; height: 152px; }

  .person { position: absolute; left: 0; right: 0; text-align: center; color: #fff; line-height: 1; }
  .person__name { top: 467px; font-size: 32px; font-weight: 600; }
  .person__title { top: 497px; font-size: 15.5px; font-weight: 400; letter-spacing: 1px; }
  .divider { position: absolute; left: 22px; right: 22px; top: 533px; height: 1px;
    background: linear-gradient(90deg, transparent, var(--rule) 20%, var(--rule) 80%, transparent); }

  .contact-list { position: absolute; left: 78px; top: 596px; list-style: none; color: #fff; font-size: 18.5px; letter-spacing: 1px; }
  .contact-list li { display: flex; align-items: center; height: 26px; }
  .contact-list svg { width: 20px; height: 18px; margin-right: 6px; }
</style>
</head>
<body>
  <section class="card card--back">
    <div class="mark-dot"></div>
    <div class="wordmark">VANTOPIPE</div>
    <div class="tagline tagline--primary">COMMERCIAL LINING SYSTEMS</div>
    <div class="tagline tagline--secondary">INSPECT / RENEW / PROTECT</div>
  </section>

  <section class="card card--front">
    <div class="wordmark">VANTOPIPE</div>
    <div class="tagline tagline--primary">COMMERCIAL LINING SYSTEMS</div>
    <div class="tagline tagline--secondary">INSPECT / RENEW / PROTECT</div>
    <div class="contact-panel"></div>
    <div class="front-ring"></div>
    <div class="mark-dot"></div>
    <div class="person person__name">MARK TOLLEN</div>
    <div class="person person__title">MANAGING PARTNER</div>
    <div class="divider"></div>
    <ul class="contact-list">
      <li>
        <svg viewBox="0 0 20 18" aria-hidden="true"><path fill="#fff" d="M4 2c1 0 1.6.3 2 1.3l1 2.2c.3.7 0 1.3-.6 1.8l-.9.7c.8 1.8 2.2 3.2 4 4l.7-.9c.5-.6 1.1-.9 1.8-.6l2.2 1c1 .4 1.3 1 1.3 2 0 1.6-1.4 3-3 3C6.7 16.5 1.5 11.3 1.5 4.5 1.5 3.2 2.6 2 4 2z"/><path fill="none" stroke="#fff" stroke-width="1.4" d="M11 2.5a5 5 0 0 1 4.5 4.5M11 5a2.5 2.5 0 0 1 2 2"/></svg>
        : 382.615.9073
      </li>
      <li>
        <svg viewBox="0 0 20 18" aria-hidden="true"><rect x="1" y="4" width="18" height="12" rx="1" fill="#fff"/><path d="M1.5 4.5 10 11l8.5-6.5" fill="none" stroke="#0067a3" stroke-width="1.5"/></svg>
        : Mark@VantoPipe.Net
      </li>
    </ul>
  </section>
</body>
</html>
```